依頼詳細
2018年の年賀状デザインを、カデノール印刷の独特の風合いを最大限に生かし、作ってください。

カデノール印刷の独特の風合いや魅力がどういったものかは、こちらの会社さんが紹介されているので参考にしてください▼
http://kamikobo-miru.examplelog.jp/2016/10/blog-post_13.html

カデノールで印刷した制作物の数々▼
https://www.fotolane.example/pim_uka/
記載項目
デザインの詳細および規定は下記のとおりです。
作成のための参考データを下記URLにアップしています。必ずダウンロードし、ご確認ください。
参考データ→http://qdl.example/bR7kLm

■内容
2018年にふさわしい年賀状デザイン
・「あけましておめでとう」「HAPPY NEW YEAR」などの賀詞
・イラスト、グラフィックなどの図柄
※名入れ印刷はしません

■サイズ
100×148mm
塗り足し可能(3mm)

■通信面、切手面(ウラオモテ)
ウラオモテのセットでデザインしてください

■印刷色
通信面(ウラ面)・・・2~4色
切手面(オモテ面)・・・1色

使える色は 基本の17色 と カスタムカラー50色 の計67色に限ります。
計67色は添付のファイルをご参照ください。

■用紙
デザインに合う紙も提案してください。提案の際はその紙に印刷したイメージを添付してもらえると嬉しいです。
紙の提案例)「クラフト系の茶色い紙」「ペラドコットン210kg」など

■納品データ形式
Illustratorでお願いいたします。画像の配置もOKです。色ごとにレイヤーを分けてください。
希望イメージ
• シンプル
複雑
• 単色
カラフル
• 暗い
明るい
• 日常
高級
• 遊び心
厳粛
• 未来的
伝統的
• 女性的
男性的
希望する色
納品ファイル
• イラストレーター形式 (.ai)
• フォトショップ形式 (.psd)
補足説明
カデノールの多色印刷では「ズレ」がポイントとなります。
色がズレても大丈夫、むしろズレたほうがいい味がでるデザインを求めます。最初からズレたデザインもOKです。
おしゃれ、かわいい、カッコいい、老若男女などジャンルは問いません。
カデノールでこんなスゴイ年賀状ができるのか!と思わせるデザインをお待ちしています。

※「カデノール」は青峰精機工業社の登録商標です
依頼公開後の追記内容
皆さま、たくさんのご応募をいただき本当にありがとうございます!
これより選考に入らせていただきます。決定までどうぞ数日お待ちください。
■ 選んだ理由

カデノール印刷に合いそうなデザインであること、
手描き感のあるイラストであること、
トレンド感のあるデザインであること
配色のバランスがよいこと
などを理由に採用させていただきました。

■ 提案者全員のお礼・コメント

皆さまこのたびは募集のテーマに賛同してくださり、素敵な作品の数々をご応募いただき誠にありがとうございました。

選定が遅くなり申し訳ありませんでしたが、たくさん迷って最後は5作品にきめさせていただきました。

また面白い企画を考えて依頼したいと思いますので、その際はまたどうぞよろしくお願いいたします。

```html
<!DOCTYPE html>
<html lang="en">
<head>
<meta charset="utf-8">
<title>Happy New Year 2018 — New Year Card</title>
<link rel="stylesheet" href="https://fonts.googleapis.com/css2?family=Archivo+Black&display=swap">
<style>
  :root {
    --paper: #f6e6da;
    --ink-purple: #4b1c8c;
    --ink-green: #3f6a2f;
    --ink-pink: #ec4f7a;
    --ink-white: #ffffff;
  }
  html, body {
    margin: 0;
    padding: 0;
    overflow: hidden;
    background: var(--paper);
  }
  .card {
    position: relative;
    width: 811px;
    height: 1200px;
    background: var(--paper);
    overflow: hidden;
  }
  .greeting {
    position: absolute;
    inset: 0;
    width: 811px;
    height: 1200px;
  }
  .greeting text {
    font-family: "Archivo Black", "Arial Black", sans-serif;
    font-size: 208px;
  }
  .greeting .offset-white { fill: var(--ink-white); }
  .greeting .offset-pink { fill: var(--ink-pink); mix-blend-mode: multiply; opacity: 0.85; }
  .ink-purple { fill: var(--ink-purple); }
  .ink-green { fill: var(--ink-green); }
  .ink-pink { fill: var(--ink-pink); }

  .pine-motif {
    position: absolute;
    left: 576px;
    top: 270px;
    width: 154px;
    height: 108px;
    background: var(--ink-green);
    border-radius: 77px 77px 10px 10px;
  }
  .plum-blossom {
    position: absolute;
    left: 60px;
    top: 400px;
    width: 136px;
    height: 136px;
    background: var(--ink-pink);
    border-radius: 50%;
  }
  .date {
    position: absolute;
    right: 49px;
    top: 556px;
    margin: 0;
    font-family: "Archivo Black", "Arial Black", sans-serif;
    font-size: 44px;
    letter-spacing: 2px;
    color: var(--ink-green);
  }
</style>
</head>
<body>
<main class="card">
  <svg class="greeting" viewBox="0 0 811 1200" role="img" aria-label="HAPPY NEW YEAR">
    <!-- misregistered white layer -->
    <g class="offset-white">
      <text x="120" y="240" textLength="644" lengthAdjust="spacingAndGlyphs">HAPPY</text>
      <text x="126" y="402" textLength="454" lengthAdjust="spacingAndGlyphs">NEW</text>
      <text x="228" y="564" textLength="514" lengthAdjust="spacingAndGlyphs">YEAR</text>
    </g>
    <!-- main inks -->
    <text x="108" y="230" textLength="644" lengthAdjust="spacingAndGlyphs"><tspan class="ink-purple">H</tspan><tspan class="ink-purple">A</tspan><tspan class="ink-purple">P</tspan><tspan class="ink-purple">P</tspan><tspan class="ink-purple">Y</tspan></text>
    <text x="114" y="392" textLength="454" lengthAdjust="spacingAndGlyphs"><tspan class="ink-green">N</tspan><tspan class="ink-pink">E</tspan><tspan class="ink-purple">W</tspan></text>
    <text x="216" y="554" textLength="514" lengthAdjust="spacingAndGlyphs"><tspan class="ink-purple">Y</tspan><tspan class="ink-green">E</tspan><tspan class="ink-purple">A</tspan><tspan class="ink-pink">R</tspan></text>
    <!-- misregistered pink accent bars -->
    <g class="offset-pink">
      <rect x="150" y="150" width="150" height="24"/>
      <rect x="430" y="100" width="110" height="22"/>
      <rect x="250" y="300" width="200" height="24" transform="rotate(-8 350 312)"/>
      <rect x="520" y="480" width="120" height="22"/>
    </g>
  </svg>

  <div class="pine-motif" role="img" aria-label="Illustration of a stylised pine branch"></div>
  <div class="plum-blossom" role="img" aria-label="Illustration of a plum blossom"></div>

  <p class="date">JAN.1.2018</p>
</main>
</body>
</html>
```